Business Card Design Project

Looking for a cool, trendy design for new business cards for our Mobile Application business.

QuillNest Apps

www.quillnestapps.example

Target Market(s)

Looking for a bold modern design that attracts a younger demographic in the mobile space.

Industry/Entity Type

Business

Requirements
Must have
• Trendy, Easily adapted for other staff cards, works with large clients but showcases and innovative company

```html
<!DOCTYPE html>
<html lang="en">
<head>
<meta charset="utf-8">
<title>QuillNest Apps – Business Card</title>
<link rel="stylesheet" href="https://fonts.googleapis.com/css2?family=Caladea&family=Open+Sans:wght@400&family=Poiret+One&display=swap">
<style>
  :root {
    --ink-deep: #071316;
    --teal-dark: #0f2a30;
    --teal-mid: #1d4a52;
    --teal-light: #2e6a72;
    --band-teal: #1b6472;
    --band-teal-edge: #0f4652;
    --title-white: #f4fbfb;
    --tagline-blue: #a8e4ee;
    --rule-grey: rgba(200, 215, 218, 0.45);
    --contact-white: #f2f6f6;
  }
  * { margin: 0; padding: 0; box-sizing: border-box; }
  html, body {
    width: 819px;
    height: 1200px;
    overflow: hidden;
    background: var(--ink-deep);
  }
  .card {
    position: relative;
    width: 819px;
    height: 1200px;
    overflow: hidden;
  }
  .texture-backdrop {
    position: absolute;
    inset: 0;
    background:
      radial-gradient(ellipse 60% 35% at 45% 8%, rgba(70,140,150,0.55), transparent 70%),
      radial-gradient(ellipse 50% 40% at 15% 55%, rgba(40,95,105,0.45), transparent 70%),
      radial-gradient(ellipse 55% 45% at 80% 95%, rgba(30,75,85,0.5), transparent 70%),
      linear-gradient(90deg, var(--teal-dark) 0%, var(--teal-mid) 25%, var(--teal-dark) 48%, var(--teal-mid) 70%, var(--teal-dark) 100%);
  }
  .brand-title {
    position: absolute;
    top: 118px;
    left: 0;
    width: 100%;
    padding-left: 16px;
    text-align: center;
    font-family: "Caladea", "Cambria", serif;
    font-size: 100px;
    line-height: 1;
    color: var(--title-white);
    text-shadow: 0 0 14px rgba(200, 240, 245, 0.55);
  }
  .tagline {
    position: absolute;
    top: 226px;
    left: 0;
    width: 100%;
    text-align: center;
    font-family: "Open Sans", "Myriad Pro", sans-serif;
    font-size: 28px;
    line-height: 1.2;
    color: var(--tagline-blue);
  }
  .name-band {
    position: absolute;
    left: 308px;
    top: 688px;
    width: 511px;
    height: 147px;
    background: linear-gradient(90deg, var(--band-teal) 0%, var(--band-teal) 70%, var(--band-teal-edge) 100%);
  }
  .name-band__label {
    position: absolute;
    left: 30px;
    top: 46px;
    font-family: "Poiret One", sans-serif;
    font-size: 50px;
    line-height: 1;
    letter-spacing: 7px;
    text-transform: uppercase;
    color: var(--contact-white);
  }
  .contact-panel {
    position: absolute;
    left: 308px;
    top: 835px;
    width: 511px;
    height: 230px;
    background: linear-gradient(180deg, rgba(0,0,0,0.85) 0%, rgba(0,0,0,0.7) 60%, rgba(0,0,0,0) 100%);
  }
  .contact-row {
    position: absolute;
    left: 328px;
    right: 0;
    border-bottom: 1px solid var(--rule-grey);
    font-family: "Open Sans", sans-serif;
    font-size: 27px;
    line-height: 1;
    color: var(--contact-white);
  }
  .contact-row span { position: absolute; bottom: 18px; }
  .contact-row--web { top: 840px; height: 65px; }
  .contact-row--web span { left: 7px; }
  .contact-row--phone { top: 905px; height: 66px; }
  .contact-row--fax { top: 971px; height: 66px; }
  .contact-row--phone span,
  .contact-row--fax span { left: 75px; }
</style>
</head>
<body>
  <main class="card">
    <div class="texture-backdrop" role="img" aria-label="Dark teal weathered metal texture with scratches and a vertical row of rivets"></div>

    <h1 class="brand-title">QuillNest Apps</h1>
    <p class="tagline">Mobile software forprofessional development</p>

    <div class="name-band">
      <span class="name-band__label">QuillNest Apps</span>
    </div>

    <div class="contact-panel"></div>
    <div class="contact-row contact-row--web"><span>www.quillnestapps.example</span></div>
    <div class="contact-row contact-row--phone"><span>ph.</span></div>
    <div class="contact-row contact-row--fax"><span>fx.</span></div>
  </main>
</body>
</html>
```